Vibrant business card design for Product person in Tech

I'm a 29 y/o female Product manager and I'd like to get a business card designed I can use when networking. I'd love something that stands out. Feel free to experiment with the use of colour, maybe geometrical elements - get creative! I work in the tech industry, so looking for a design without too much of a corporate feel. <br/><br/>The business card should have room for:<br/>Name<br/>Email address<br/>Veltrio

Target Market(s)

Tech

Contact Information for Business Card

Name
Email
Veltrio

Colors
faa54b
00a990
33b8a4
abd037
fbee3f
e667a6
ffcf3e
f59195

```html
<!DOCTYPE html>
<html lang="en">
<head>
<meta charset="utf-8">
<title>Business Card – Daniel Brooks</title>
<link href="https://fonts.googleapis.com/css2?family=Montserrat:wght@400;500;600&display=swap" rel="stylesheet">
<style>
  :root {
    --stage: #222222;
    --teal: #00a990;
    --teal-light: #33b8a4;
    --pink: #e667a6;
    --pink-soft: #f59195;
    --orange: #faa54b;
    --yellow: #fbee3f;
    --gold: #ffcf3e;
    --lime: #abd037;
    --white: #ffffff;
  }
  * { margin: 0; padding: 0; box-sizing: border-box; }
  html, body {
    width: 1200px; height: 900px; overflow: hidden;
    background: var(--stage);
    font-family: "Montserrat", sans-serif;
  }
  .canvas { position: relative; width: 1200px; height: 900px; }

  .card {
    position: absolute;
    width: 640px; height: 366px;
    overflow: hidden;
    box-shadow: 0 18px 40px rgba(0,0,0,.5);
  }

  /* Front face */
  .card--front { left: 110px; top: 48px; background: var(--teal); }
  .card--front .texture {
    position: absolute; inset: 0;
    background: radial-gradient(ellipse at 30% 40%, var(--teal-light) 0%, var(--teal) 70%);
  }
  .card--front .accent-band {
    position: absolute; left: 0; right: 0; bottom: 0; height: 10px;
    background: linear-gradient(90deg, var(--orange), var(--gold), var(--lime), var(--pink));
  }
  .brand {
    position: absolute;
    display: flex; align-items: center; gap: 18px;
    white-space: nowrap;
  }
  .brand__mark {
    width: 70px; height: 70px; border-radius: 50%;
    background: var(--white); flex: none;
  }
  .brand__name {
    font-weight: 500; font-size: 38px; letter-spacing: 1px;
    color: var(--white); line-height: 1;
  }
  .brand__tagline {
    font-size: 13px; letter-spacing: 1.5px; color: var(--yellow);
    margin-top: 6px;
  }
  .card--front .brand { left: 50%; top: 50%; transform: translate(-50%, -50%); }

  /* Back face */
  .card--back {
    left: 450px; top: 480px;
    background: var(--pink);
    border: 4px solid var(--orange);
  }
  .card--back .brand { left: 60px; top: 44px; gap: 14px; }
  .card--back .brand__mark { width: 54px; height: 54px; background: var(--yellow); }
  .card--back .brand__name { font-size: 28px; }
  .card--back .brand__tagline { font-size: 11px; margin-top: 4px; }

  .person { position: absolute; left: 60px; top: 140px; }
  .person__name {
    font-weight: 600; font-size: 36px; letter-spacing: 1px;
    color: var(--white); line-height: 1;
  }
  .person__role { font-size: 16px; color: var(--yellow); margin-top: 6px; }

  .divider {
    position: absolute; left: 60px; right: 60px; height: 2px;
    background: var(--gold);
  }
  .divider--top { top: 222px; }
  .divider--bottom { top: 336px; }

  .contacts {
    position: absolute; left: 60px; top: 240px;
    list-style: none; display: flex; flex-direction: column; gap: 14px;
  }
  .contact {
    display: flex; align-items: center; gap: 16px;
    color: var(--white); font-size: 19px;
  }
  .contact__icon { width: 28px; height: 28px; flex: none; }
  .contact__dot {
    width: 28px; height: 28px; border-radius: 50%; background: var(--yellow); flex: none;
  }
</style>
</head>
<body>
<main class="canvas">

  <section class="card card--front">
    <div class="texture" role="img" aria-label="Faint network pattern of joined dots and lines on teal"></div>
    <div class="accent-band"></div>
    <div class="brand">
      <span class="brand__mark"></span>
      <div>
        <p class="brand__name">LOGO DESIGN</p>
        <p class="brand__tagline">YOUR TAGLINE</p>
      </div>
    </div>
  </section>

  <section class="card card--back">
    <div class="brand">
      <span class="brand__mark"></span>
      <div>
        <p class="brand__name">LOGO DESIGN</p>
        <p class="brand__tagline">YOUR TAGLINE</p>
      </div>
    </div>

    <div class="person">
      <h1 class="person__name">DANIEL BROOKS</h1>
      <p class="person__role">Product Manager</p>
    </div>

    <div class="divider divider--top"></div>

    <ul class="contacts">
      <li class="contact">
        <svg class="contact__icon" viewBox="0 0 28 28" aria-hidden="true">
          <rect x="2" y="6" width="24" height="16" fill="#fbee3f"/>
          <polyline points="2,6 14,16 26,6" fill="none" stroke="#e667a6" stroke-width="2"/>
        </svg>
        <span>danielbrooks@mailora.com</span>
      </li>
      <li class="contact">
        <span class="contact__dot"></span>
        <span>veltrio/daniel.brooks</span>
      </li>
    </ul>

    <div class="divider divider--bottom"></div>
  </section>

</main>
</body>
</html>
```